I need a logo design and a business card design for a new strategy consultancy that I set up called Corvanel LLC. We help clients make strategically important decisions, cutting through the cloud of noise. The design should imply clarity, simplicity and wisdom.

```html
<!DOCTYPE html>
<html lang="en">
<head>
<meta charset="utf-8">
<title>Corvanel LLC — Business Card</title>
<link rel="stylesheet" href="https://fonts.googleapis.com/css2?family=Cinzel:wght@400;600&family=Tinos&display=swap">
<style>
  :root {
    --page: #e6e7e9;
    --card-dark: #58585b;
    --card-light: #ffffff;
    --ink: #3d3d40;
    --ink-soft: #8a8a8e;
    --ink-on-dark: #d7d8da;
    --accent: #1ea7e6;
    --rule: #9a9a9e;
  }
  * { margin: 0; padding: 0; box-sizing: border-box; }
  html, body { width: 1200px; height: 905px; overflow: hidden; background: var(--page); }
  .stage {
    width: 1200px; height: 905px;
    display: flex; flex-direction: column; align-items: center; justify-content: center; gap: 44px;
  }
  .card {
    position: relative; width: 640px; height: 366px;
    box-shadow: 0 8px 24px rgba(0,0,0,.18);
  }
  .card--front { background: var(--card-dark); display: flex; align-items: center; justify-content: center; }
  .card--back { background: var(--card-light); }

  .brand { display: flex; align-items: center; gap: 14px; }
  .brand__dot { width: 18px; height: 18px; border-radius: 50%; background: var(--accent); flex: none; }
  .brand__text { display: flex; flex-direction: column; }
  .brand__name {
    font-family: "Cinzel", serif; font-weight: 400; font-size: 34px; letter-spacing: 1px; line-height: 1;
  }
  .brand__tagline {
    font-family: "Cinzel", serif; font-weight: 400; font-size: 12.5px; letter-spacing: 3.6px; margin-top: 6px;
  }
  .card--front .brand__name { color: var(--ink-on-dark); }
  .card--front .brand__tagline { color: var(--ink-on-dark); opacity: .75; }
  .card--back .brand { position: absolute; top: 42px; right: 36px; }
  .card--back .brand__name { color: var(--ink); }
  .card--back .brand__tagline { color: var(--ink-soft); }

  .person { position: absolute; left: 36px; top: 118px; }
  .person__name { font-family: "Cinzel", serif; font-weight: 600; font-size: 19px; letter-spacing: 1px; color: var(--ink); }
  .person__role { font-family: "Cinzel", serif; font-weight: 600; font-size: 17px; letter-spacing: 1px; color: var(--accent); margin-top: 2px; }

  .rule { position: absolute; height: 1px; background: var(--rule); }
  .rule--main { left: 300px; right: 30px; top: 132px; }
  .rule--contact { left: 36px; width: 180px; top: 232px; }

  .address {
    position: absolute; right: 36px; top: 150px; text-align: right;
    font-family: "Tinos", serif; font-size: 17px; line-height: 1.3; color: var(--ink);
  }
  .contacts { position: absolute; left: 36px; top: 246px; list-style: none; }
  .contacts li {
    display: flex; align-items: center; gap: 12px;
    font-family: "Tinos", serif; font-size: 19px; line-height: 26px; color: var(--ink);
  }
  .contacts svg { width: 18px; height: 18px; fill: var(--accent); flex: none; }
</style>
</head>
<body>
<main class="stage">
  <section class="card card--front">
    <div class="brand">
      <span class="brand__dot"></span>
      <div class="brand__text">
        <span class="brand__name">CORVANEL LLC</span>
        <span class="brand__tagline">STRATEGY CONSULTANCY</span>
      </div>
    </div>
  </section>

  <section class="card card--back">
    <div class="brand">
      <span class="brand__dot"></span>
      <div class="brand__text">
        <span class="brand__name">CORVANEL LLC</span>
        <span class="brand__tagline">STRATEGY CONSULTANCY</span>
      </div>
    </div>

    <div class="person">
      <p class="person__name">ELLIOT MARSDEN</p>
      <p class="person__role">CEO/FOUNDER</p>
    </div>

    <div class="rule rule--main"></div>

    <p class="address">428 W. Harbor Lane<br>Suite B, Ardenvale, CA 92614</p>

    <div class="rule rule--contact"></div>

    <ul class="contacts">
      <li>
        <svg viewBox="0 0 24 24" aria-hidden="true"><path d="M6.6 10.8a15.1 15.1 0 0 0 6.6 6.6l2.2-2.2c.3-.3.7-.4 1-.2 1.1.4 2.3.6 3.6.6.6 0 1 .4 1 1V20c0 .6-.4 1-1 1A17 17 0 0 1 3 4c0-.6.4-1 1-1h3.5c.6 0 1 .4 1 1 0 1.3.2 2.5.6 3.6.1.3 0 .7-.2 1z"/></svg>
        <span>230.555.0142</span>
      </li>
      <li>
        <svg viewBox="0 0 24 24" aria-hidden="true"><path d="M6 2h12v5H6zM3 8h18a2 2 0 0 1 2 2v7h-4v5H5v-5H1v-7a2 2 0 0 1 2-2zm4 8v4h10v-4z"/></svg>
        <span>230.555.0178</span>
      </li>
      <li>
        <svg viewBox="0 0 24 24" aria-hidden="true"><path d="M2 5h20v14H2zm2 2v.5l8 5.5 8-5.5V7L12 12.5z"/></svg>
        <span>elliot@corvanel.com</span>
      </li>
      <li>
        <svg viewBox="0 0 24 24" aria-hidden="true"><path d="M12 2a10 10 0 1 0 0 20 10 10 0 0 0 0-20zm6.9 6h-3a15 15 0 0 0-1.3-4A8 8 0 0 1 18.9 8zM12 4c.8 1.1 1.5 2.5 1.9 4h-3.8c.4-1.5 1.1-2.9 1.9-4zM4.3 14a8 8 0 0 1 0-4h3.4a16 16 0 0 0 0 4zm.8 2h3a15 15 0 0 0 1.3 4A8 8 0 0 1 5.1 16zm3-8h-3a8 8 0 0 1 4.3-4 15 15 0 0 0-1.3 4zM12 20c-.8-1.1-1.5-2.5-1.9-4h3.8c-.4 1.5-1.1 2.9-1.9 4zm2.3-6H9.7a14 14 0 0 1 0-4h4.6a14 14 0 0 1 0 4zm.3 6a15 15 0 0 0 1.3-4h3a8 8 0 0 1-4.3 4zm1.7-6a16 16 0 0 0 0-4h3.4a8 8 0 0 1 0 4z"/></svg>
        <span>www.corvanel.com</span>
      </li>
    </ul>
  </section>
</main>
</body>
</html>
```